Plumbing & Heating company

A leaflet containing -

Company name - Brackenfold Plumbing Solutions
logo
Mobile number - 07700 914226
Landline - 01632 870512
Email - Info@brackenfoldplumbing.example.co.uk
website - Brackenfold-plumbing.example.co.uk
Social media logos - pixgram, Chatterly

services we offer

- Boiler replacements (free quote)
- General plumbing & heating
- Tap replacements
- 1st & 2nd
- New builds & Extensions
- Cylinder replcemets

```html
<!DOCTYPE html>
<html lang="en">
<head>
<meta charset="utf-8">
<title>Brackenfold Plumbing Solutions – Leaflet</title>
<link rel="stylesheet" href="https://fonts.googleapis.com/css2?family=Poppins:wght@400;500;600;700;800&display=swap">
<style>
:root{
  --blue:#2a5a9e;
  --blue-dark:#1f4a86;
  --red:#ef4c3c;
  --ink:#2b2b2b;
  --footer:#4a4a4a;
  --band:#eef0f3;
  --gold:#f2b51b;
  --stage:#f3f3f3;
}
*{margin:0;padding:0;box-sizing:border-box}
html,body{width:766px;height:1200px;overflow:hidden;background:var(--stage);font-family:'Poppins',sans-serif;color:var(--ink)}
.page{position:absolute;left:158px;width:450px;height:582px;background:#fff;overflow:hidden}
.page--front{top:12px}
.page--back{top:606px}
.shapes{position:absolute;left:0;top:0}
.abs{position:absolute}

/* wordmark */
.wordmark{position:absolute;color:var(--blue);font-weight:700;line-height:1.05;display:flex;align-items:center;gap:6px}
.wordmark__dot{width:10px;height:10px;border-radius:50%;background:var(--red);flex:none}
.wordmark__name{font-size:19px;letter-spacing:.5px;display:block}
.wordmark__sub{font-size:8.5px;letter-spacing:2.2px;display:block}
.wordmark--back .wordmark__name{font-size:13px}
.wordmark--back .wordmark__sub{font-size:6px;letter-spacing:1.5px}
.wordmark--back .wordmark__dot{width:8px;height:8px}

/* photo placeholders */
.photo{position:absolute;border-radius:50%}
.photo--hero{left:95px;top:113px;width:256px;height:256px;background:radial-gradient(circle at 40% 40%,#c9ced6,#6f7a88 60%,#2c3440);box-shadow:-7px -5px 0 var(--red)}
.photo--boiler{left:11px;top:273px;width:108px;height:108px;background:radial-gradient(circle at 50% 45%,#e9ecef,#9a7652 55%,#6b4a2e);box-shadow:-4px -3px 0 var(--red)}
.photo--pipes{left:308px;top:232px;width:140px;height:140px;background:radial-gradient(circle at 50% 50%,#d79a6a,#a27a55 55%,#6e5640);box-shadow:-5px -5px 0 var(--red)}

/* front hero text */
.hero-kicker{left:0;width:450px;top:403px;text-align:center;color:#fff;font-size:11px;font-weight:600;letter-spacing:3.2px}
.hero-title{left:0;width:450px;top:418px;text-align:center;font-weight:800;font-size:31px;line-height:1;letter-spacing:-.3px}
.hero-title .accent{color:var(--red);display:block}
.hero-title .light{color:#fff;display:block;margin-top:2px}
.feature-row{left:84px;top:490px;display:flex;gap:8px}
.feature{display:flex;align-items:center;gap:5px;color:#fff;font-size:7.6px;line-height:1.3}
.feature__icon{width:19px;height:19px;border-radius:50%;background:#fff;flex:none;display:flex;align-items:center;justify-content:center}

/* footer */
.footer{position:absolute;left:0;top:536px;width:450px;height:46px}
.badge{position:absolute;background:#fff;border-radius:2px}
.badge--register{left:28px;top:9px;width:57px;height:24px}
.badge--partner{left:97px;top:7px;width:31px;height:31px;border:2px solid #2f8a4a}
.register-no{position:absolute;left:27px;top:36px;font-size:4.3px;color:#fff;font-weight:700}
.contact{position:absolute;color:#fff;font-size:6.2px;line-height:1.45;display:flex;align-items:flex-start;gap:3px}
.contact svg{flex:none;margin-top:1px}
.contact--phone{left:170px;top:14px;font-size:6.6px;font-weight:500}
.contact--mail{left:262px;top:12px;font-size:5.2px}
.social{position:absolute;left:385px;top:14px;display:flex;flex-direction:column;gap:3px;color:#fff;font-size:5.6px}
.social span{display:flex;align-items:center;gap:3px}
.social i{display:block;width:6px;height:6px;background:#fff;border-radius:1px}

/* back page */
.about{left:29px;top:98px;width:235px;color:#fff}
.section-title{font-weight:700;font-size:13px;letter-spacing:-.2px}
.about .section-title{color:var(--red);font-size:11px}
.about p{font-size:6.5px;line-height:1.36;margin-top:2px}
.about p+p{margin-top:8px}
.services-title{left:32px;top:215px;color:var(--blue)}
.service{position:absolute;display:flex;align-items:center;gap:10px;font-weight:600;font-size:9.6px;line-height:1.05;color:var(--ink)}
.service__photo{width:40px;height:40px;border-radius:50%;flex:none;box-shadow:-2px 0 0 var(--red)}
.rule{position:absolute;left:26px;width:398px;border-top:1px dashed #9aa0a8}
.band{position:absolute;left:0;top:404px;width:450px;height:132px;background:var(--band)}
.clients-title{left:32px;top:412px;color:var(--blue)}
.review{position:absolute;border:1px solid var(--blue);border-top:none;border-radius:0 0 3px 3px;padding:6px 5px 4px;font-size:4.6px;line-height:1.3;font-weight:500}
.review__q{position:absolute;top:-11px;left:0;color:var(--blue);font-size:22px;font-weight:800;line-height:1}
.review__q--end{top:auto;bottom:-14px;left:auto;right:-14px}
.review__meta{display:flex;justify-content:space-between;margin-top:3px;font-size:4.6px;color:var(--red);font-weight:600}
.review__stars{color:var(--gold);letter-spacing:.5px;font-size:6px;margin-right:10px}
.cta{position:absolute;left:98px;top:522px;width:257px;height:16px;border-radius:8px;background:var(--blue);color:#fff;font-size:7.4px;font-weight:700;text-align:center;line-height:16px;z-index:2}
</style>
</head>
<body>

<section class="page page--front">
  <svg class="shapes" width="450" height="582" viewBox="0 0 450 582">
    <path d="M0 392 C20 352 70 330 130 332 L330 332 C380 332 425 322 450 318 V536 H0 Z" fill="var(--blue)"/>
    <path d="M2 398 C18 370 30 356 44 348" stroke="#fff" stroke-width="2" fill="none"/>
    <path d="M416 322 C432 334 442 346 450 358" stroke="#fff" stroke-width="2" fill="none"/>
  </svg>

  <div class="wordmark" style="left:0;top:28px;width:450px;justify-content:center">
    <span class="wordmark__dot"></span>
    <span><span class="wordmark__name">BRACKENFOLD</span><span class="wordmark__sub">PLUMBING SOLUTIONS</span></span>
  </div>

  <div class="photo photo--hero" role="img" aria-label="Plumber in a blue hard hat and safety glasses adjusting pipework with a wrench"></div>
  <div class="photo photo--boiler" role="img" aria-label="Wall-mounted boiler with pipework on a timber wall"></div>
  <div class="photo photo--pipes" role="img" aria-label="Copper pipe first fix running through timber studwork"></div>

  <div class="abs hero-kicker">BRACKENFOLD PLUMBING SOLUTIONS</div>
  <h1 class="abs hero-title"><span class="accent">SYSTEM DESIGN &amp;</span><span class="light">INSTALLATION</span></h1>

  <div class="abs feature-row">
    <div class="feature"><span class="feature__icon"><svg width="11" height="11" viewBox="0 0 12 12"><path d="M2 10 L7 5 M7 5 a2.5 2.5 0 1 0 2-3" stroke="var(--blue)" stroke-width="1.4" fill="none" stroke-linecap="round"/></svg></span><span>New Build &amp;<br>Redevelopments</span></div>
    <div class="feature"><span class="feature__icon"><svg width="11" height="11" viewBox="0 0 12 12"><rect x="2" y="3" width="3" height="7" fill="none" stroke="var(--blue)" stroke-width="1.2"/><rect x="7" y="2" width="3" height="8" fill="none" stroke="var(--blue)" stroke-width="1.2"/></svg></span><span>General Plumbing<br>&amp; Heating</span></div>
    <div class="feature"><span class="feature__icon"><svg width="11" height="11" viewBox="0 0 12 12"><path d="M2 4 H8 V7 M5 2 V4 M8 8.5 V10" stroke="var(--blue)" stroke-width="1.3" fill="none" stroke-linecap="round"/></svg></span><span>Tap<br>Replacements</span></div>
  </div>

  <div class="footer">
    <svg class="shapes" width="450" height="46" viewBox="0 0 450 46">
      <rect width="450" height="46" fill="var(--footer)"/>
      <path d="M0 0 H142 Q158 0 166 46 H0 Z" fill="var(--red)"/>
    </svg>
    <div class="badge badge--register" role="img" aria-label="Heating safety register badge"></div>
    <div class="badge badge--partner" role="img" aria-label="Manufacturer partner badge"></div>
    <div class="register-no">HEATSAFE REGISTER: 7310482</div>
    <div class="contact contact--phone"><svg width="6" height="6" viewBox="0 0 10 10"><path d="M2 1 L4 3 L3 4.5 Q4.5 6.5 5.5 7 L7 6 L9 8 L7.5 9.5 Q1 7 0.5 2.5 Z" fill="var(--red)"/></svg><span>07700 914226/<br>01632 870512</span></div>
    <div class="contact contact--mail"><span>
      <span style="display:flex;gap:3px;align-items:center"><svg width="6" height="5" viewBox="0 0 10 8"><rect width="10" height="8" rx="1" fill="var(--red)"/><path d="M0.5 1 L5 4.5 L9.5 1" stroke="#fff" fill="none"/></svg>Info@brackenfoldplumbing.example.co.uk</span>
      <span style="display:flex;gap:3px;align-items:center;margin-top:3px"><svg width="6" height="6" viewBox="0 0 10 10"><circle cx="5" cy="5" r="4.3" fill="none" stroke="var(--red)" stroke-width="1.2"/></svg>www.brackenfold-plumbing.example.co.uk</span>
    </span></div>
    <div class="social"><span><i></i>pixgram</span><span><i></i>Chatterly</span></div>
  </div>
</section>

<section class="page page--back">
  <svg class="shapes" width="450" height="582" viewBox="0 0 450 582">
    <defs>
      <linearGradient id="boilerPhoto" x1="0" y1="0" x2="1" y2="1">
        <stop offset="0" stop-color="#e7e5e1"/>
        <stop offset=".6" stop-color="#d2cdc6"/>
        <stop offset="1" stop-color="#b88a62"/>
      </linearGradient>
    </defs>
    <path d="M238 182 Q340 200 450 150 V178 Q360 212 268 200 Q248 194 238 182 Z" fill="var(--red)"/>
    <path d="M0 66 Q170 76 222 22 Q236 6 244 0 H450 V150 Q360 190 250 184 Q130 182 0 198 Z" fill="var(--blue)"/>
    <path d="M246 0 H450 V150 Q380 170 322 150 Q258 130 248 70 Q244 30 246 0 Z" fill="#3aa0e0"/>
    <path d="M252 0 H450 V144 Q380 164 324 145 Q264 126 254 70 Q250 30 252 0 Z" fill="url(#boilerPhoto)" role="img" aria-label="Installed white boiler above a hot water cylinder with copper pipework"/>
  </svg>

  <div class="wordmark wordmark--back" style="left:30px;top:18px">
    <span class="wordmark__dot"></span>
    <span><span class="wordmark__name">BRACKENFOLD</span><span class="wordmark__sub">PLUMBING SOLUTIONS</span></span>
  </div>

  <div class="abs about">
    <h2 class="section-title">ABOUT US</h2>
    <p>Brackenfold Plumbing Solutions are a young and ambitious Plumbing &amp; Heating company with close to a decade of experience. We are specialists in System design &amp; installation – 1st &amp; 2nd fix, and have a considerable experience in both new build and refurbishment projects including domestic, commercial and listed properties.</p>
    <p>We offer a wide range of services covering Winchester and the surrounding areas.</p>
  </div>

  <h2 class="abs section-title services-title">OUR SERVICES</h2>

  <div class="service" style="left:32px;top:246px"><span class="service__photo" role="img" aria-label="Copper pipes in timber floor joists" style="background:radial-gradient(circle,#c98a5c,#6b4b35)"></span>New Build &amp;<br>Redevelopments</div>
  <div class="service" style="left:210px;top:246px"><span class="service__photo" role="img" aria-label="Hands fitting plumbing parts" style="background:radial-gradient(circle,#b59a84,#4e4b4c)"></span>General plumbing &amp;<br>heating</div>
  <div class="rule" style="top:292px"></div>
  <div class="service" style="left:32px;top:297px"><span class="service__photo" role="img" aria-label="First fix pipework in a wall" style="background:radial-gradient(circle,#d9dcdf,#6e7378)"></span>1st &amp; 2nd Fix</div>
  <div class="service" style="left:210px;top:297px"><span class="service__photo" role="img" aria-label="Hand fitting a chrome tap" style="background:radial-gradient(circle,#e0c1b3,#7a7f86)"></span>Tap<br>Replacements</div>
  <div class="rule" style="top:346px"></div>
  <div class="service" style="left:32px;top:351px"><span class="service__photo" role="img" aria-label="Boiler on a wooden wall" style="background:radial-gradient(circle,#ece7e0,#9a7550)"></span>Boiler<br>Replacements</div>
  <div class="service" style="left:210px;top:351px"><span class="service__photo" role="img" aria-label="Hot water cylinder with fittings" style="background:radial-gradient(circle,#dcd5cc,#6f5a48)"></span>Cylinder<br>Replcemets</div>

  <div class="band"></div>
  <h2 class="abs section-title clients-title">WHAT OUR CLIENTS ARE SAYING</h2>

  <div class="review" style="left:66px;top:444px;width:146px">
    <span class="review__q">“</span>
    Absolutely fantastic service would highly recommend tom came out to 1st and 2nd fix our kitchen, can honestly say he's so neat and tidy with his pipe work it looks amazing he fits in around the times that suits you best too top job
    <div class="review__meta"><span>Kitchen 1st and 2nd fix</span><span class="review__stars">★★★★★</span></div>
    <span class="review__q review__q--end">”</span>
  </div>
  <div class="review" style="left:239px;top:444px;width:145px">
    <span class="review__q">“</span>
    Tom was very quick to respond, quote and fit our outdoor shower and was very clean/tidy whilst doing the work. Tom has also since done some sealing on an indoor shower of ours, which was very neatly done. We will certainly be using BPS in the future for any plumbing related jobs, highly recommend Tom!
    <div class="review__meta"><span>Outdoor Shower</span><span class="review__stars">★★★★★</span></div>
    <span class="review__q review__q--end">”</span>
  </div>

  <div class="cta">CONTACT US TODAY TO GET A FREE QUOTE</div>

  <div class="footer">
    <svg class="shapes" width="450" height="46" viewBox="0 0 450 46">
      <rect width="450" height="46" fill="var(--footer)"/>
      <path d="M0 0 H142 Q158 0 166 46 H0 Z" fill="var(--red)"/>
    </svg>
    <div class="badge badge--register" role="img" aria-label="Heating safety register badge"></div>
    <div class="badge badge--partner" role="img" aria-label="Manufacturer partner badge"></div>
    <div class="register-no">HEATSAFE REGISTER: 7310482</div>
    <div class="contact contact--phone"><svg width="6" height="6" viewBox="0 0 10 10"><path d="M2 1 L4 3 L3 4.5 Q4.5 6.5 5.5 7 L7 6 L9 8 L7.5 9.5 Q1 7 0.5 2.5 Z" fill="var(--red)"/></svg><span>07700 914226/<br>01632 870512</span></div>
    <div class="contact contact--mail"><span>
      <span style="display:flex;gap:3px;align-items:center"><svg width="6" height="5" viewBox="0 0 10 8"><rect width="10" height="8" rx="1" fill="var(--red)"/><path d="M0.5 1 L5 4.5 L9.5 1" stroke="#fff" fill="none"/></svg>Info@brackenfoldplumbing.example.co.uk</span>
      <span style="display:flex;gap:3px;align-items:center;margin-top:3px"><svg width="6" height="6" viewBox="0 0 10 10"><circle cx="5" cy="5" r="4.3" fill="none" stroke="var(--red)" stroke-width="1.2"/></svg>www.brackenfold-plumbing.example.co.uk</span>
    </span></div>
    <div class="social"><span><i></i>pixgram</span><span><i></i>Chatterly</span></div>
  </div>
</section>

</body>
</html>
```